Clever & creative business card needed for a pediatric dentist.

We need a business card for a pediatric dentist that is building a brand-new pediatric dental practice. He is funny, outgoing, and sociable, and he hopes to give his business card to dentists and pediatricians so that he can give them information of where to refer infants, children, and teenagers that need high quality and attainable dental care.

The name of the dental practice is Copper Fern Pediatric Dentistry. Logo design .png / .pdf/ .jpg are provided to aid in the design.

The dentist's last name is Tolvan (which sounds like "burger", as in "hamburger” or “cheeseburger"). Since it is pediatric practice, kudos will be given to designs that implement a little joke into the design - but hopefully in a small or hidden way (such as putting something like a cheeseburger on the back of the card, or hiding it an an abstract way).

Thank you!

Please make a design that incorporates colors. It should be fun! Not too serious. It does not have to follow the color scheme of the logos.

```html
<!DOCTYPE html>
<html lang="en">
<head>
<meta charset="utf-8">
<title>Copper Fern Pediatric Dentistry – Business Card</title>
<link href="https://fonts.googleapis.com/css2?family=Montserrat:wght@600&family=Questrial&display=swap" rel="stylesheet">
<style>
  :root {
    --page: #e6e7e8;
    --card: #39393b;
    --text: #f2f2f2;
    --green: #5cbd78;
    --mint-light: #b5ddb3;
    --mint: #8fcd92;
    --green-deep: #33a05f;
  }
  * { margin: 0; padding: 0; box-sizing: border-box; }
  html, body {
    width: 1200px; height: 1116px; overflow: hidden;
    background: var(--page);
    font-family: "Questrial", sans-serif;
    color: var(--text);
  }
  .card {
    position: absolute; top: 444px;
    width: 390px; height: 223px;
    background: var(--card);
    overflow: hidden;
  }
  .card--front { left: 188px; }
  .card--back { left: 618px; }

  .holder-name {
    position: absolute; left: 15px; top: 33px;
    font-family: "Montserrat", sans-serif; font-weight: 600;
    font-size: 18px; color: var(--green); letter-spacing: 0.2px;
  }
  .holder-role { position: absolute; left: 15px; top: 52px; font-size: 11.5px; }

  .contact-list { position: absolute; left: 15px; top: 88px; list-style: none; }
  .contact-list li {
    display: flex; align-items: center; gap: 6px;
    font-size: 11.5px; line-height: 13.6px;
  }
  .contact-list svg { width: 9px; height: 9px; flex: none; }

  .divider {
    position: absolute; left: 15px; top: 155px;
    width: 10px; height: 1px; background: var(--green);
  }
  .address { position: absolute; left: 15px; top: 169px; font-size: 11.5px; line-height: 13.4px; }

  .decor {
    position: absolute; top: 0; height: 223px; width: 124px;
    background: linear-gradient(135deg, var(--mint-light) 0%, var(--mint) 40%, var(--green) 70%, var(--green-deep) 100%);
  }
  .decor--front { right: 0; border-top-left-radius: 40px 60px; border-bottom-left-radius: 70px 100px; }
  .decor--back { left: 0; border-top-right-radius: 40px 60px; border-bottom-right-radius: 70px 100px;
    background: linear-gradient(225deg, var(--mint-light) 0%, var(--mint) 40%, var(--green) 70%, var(--green-deep) 100%); }

  .brand {
    position: absolute; left: 200px; width: 160px; top: 92px;
    text-align: center;
  }
  .brand-dot {
    width: 30px; height: 30px; border-radius: 50%;
    background: var(--green); margin: 0 auto 14px;
  }
  .brand-name { font-size: 22px; line-height: 22px; color: var(--text); }
  .brand-name span { display: block; font-size: 8px; line-height: 14px; letter-spacing: 2.6px; }
</style>
</head>
<body>
  <section class="card card--front">
    <h1 class="holder-name">Marek Tolvan</h1>
    <p class="holder-role">Owner/ CEO</p>
    <ul class="contact-list">
      <li><svg viewBox="0 0 10 10"><path d="M2 1l2 2-1 1.2c.6 1.2 1.5 2.1 2.8 2.8L7 6l2 2-1.3 1.3C4.5 9 1 5.5.7 2.3z" fill="var(--green)"/></svg>(09) 5550 1482</li>
      <li><svg viewBox="0 0 10 10"><rect x="2.5" y="0.5" width="5" height="9" rx="1" fill="none" stroke="var(--green)"/></svg>(09) 5550 1482</li>
      <li><svg viewBox="0 0 10 10"><rect x="0.5" y="2" width="9" height="6" fill="var(--green)"/><path d="M.5 2L5 5.5 9.5 2" fill="none" stroke="var(--card)" stroke-width=".8"/></svg>marek@copperfern.com</li>
      <li><svg viewBox="0 0 10 10"><circle cx="5" cy="5" r="4.3" fill="var(--green)"/><path d="M.7 5h8.6M5 .7v8.6M5 .7c-2.4 2.4-2.4 6.2 0 8.6M5 .7c2.4 2.4 2.4 6.2 0 8.6" fill="none" stroke="var(--card)" stroke-width=".6"/></svg>www.copperfern.com</li>
    </ul>
    <div class="divider"></div>
    <p class="address">0/00 Larkspur Ave<br>Elmsfield, 0000</p>
    <div class="decor decor--front" role="img" aria-label="Large layered green tooth emblem, cropped at card edge"></div>
  </section>

  <section class="card card--back">
    <div class="decor decor--back" role="img" aria-label="Large layered green tooth emblem, cropped at card edge"></div>
    <div class="brand">
      <div class="brand-dot"></div>
      <p class="brand-name">copper fern<span>PEDIATRIC DENTISTRY</span></p>
    </div>
  </section>
</body>
</html>
```